Business Podcaster needs a sexy book cover design for upcoming book launch

I'm launching a book called Chase the Summit: how to accelerate your growth through reaching out, getting a response from, and leaving an impression on the people you admire most. It would be cool to have maybe a band of heroes or a single hero or something on the cover, then I'll need the spine designed, as well as the back cover which would be mostly just quotes about the book from other prominent people.

I dont want to extend it. I want to shorten it. Can I do that?

```html
<!DOCTYPE html>
<html lang="en">
<head>
<meta charset="utf-8">
<title>Chase the Summit – Book Cover Wrap</title>
<link href="https://fonts.googleapis.com/css2?family=Bangers&family=Bebas+Neue&family=Jost:wght@400&display=swap" rel="stylesheet">
<style>
  :root {
    --ink: #000000;
    --paper: #ffffff;
    --hero-yellow: #fff200;
    --hero-red: #ff1a1a;
    --sky-amber: #c99a6a;
    --sky-violet: #8a6a8a;
    --cape-red: #a3121c;
    --suit-navy: #2a2a3a;
    --chest-blue: #1a4fd0;
  }
  * { box-sizing: border-box; margin: 0; padding: 0; }
  html, body { width: 1200px; height: 855px; overflow: hidden; background: var(--ink); }
  .cover-wrap { position: relative; width: 1200px; height: 855px; background: var(--ink); color: var(--paper); }

  /* Title lockup */
  .title-lockup {
    position: absolute;
    font-family: "Bangers", system-ui, sans-serif;
    color: var(--hero-yellow);
    text-transform: uppercase;
    line-height: 0.86;
    -webkit-text-stroke: 2px var(--ink);
    paint-order: stroke fill;
    text-shadow: 4px 4px 0 var(--paper), 5px 5px 0 var(--ink);
    text-align: center;
  }
  .title-lockup .title-small {
    display: block;
    color: var(--ink);
    -webkit-text-stroke: 0;
    text-shadow: none;
    letter-spacing: 0.02em;
  }
  .title-lockup .title-line { display: block; }

  /* Back cover */
  .back-cover { position: absolute; left: 0; top: 0; width: 579px; height: 855px; }
  .back-title { left: 37px; top: 38px; width: 210px; }
  .back-title .title-line.first { font-size: 84px; }
  .back-title .title-small { font-size: 22px; margin: 2px 0; }
  .back-title .title-line.second { font-size: 72px; }
  .back-copy {
    position: absolute; left: 37px; top: 46px; width: 503px;
    font-family: "Jost", system-ui, sans-serif;
    font-size: 13px; line-height: 13.95px; text-align: justify; hyphens: auto;
  }
  .back-copy .logo-space { float: left; width: 229px; height: 209px; }
  .back-copy p + p { margin-top: 14px; }

  /* Spine */
  .spine { position: absolute; left: 579px; top: 0; width: 46px; height: 855px; }
  .spine-title, .spine-author {
    position: absolute; left: 50%; white-space: nowrap;
    transform-origin: 0 0; transform: rotate(90deg) translateY(-50%);
  }
  .spine-title {
    top: 74px;
    font-family: "Bangers", system-ui, sans-serif; font-size: 48px; letter-spacing: 0.06em;
    color: var(--hero-yellow);
  }
  .spine-title .accent { color: var(--hero-red); }
  .spine-author {
    top: 537px;
    font-family: "Bebas Neue", system-ui, sans-serif; font-size: 44px; color: var(--paper);
  }

  /* Front cover */
  .front-cover { position: absolute; left: 631px; top: 0; width: 569px; height: 855px; }
  .hero-photo { position: absolute; left: 0; top: 76px; width: 569px; height: 470px; }
  .front-author {
    position: absolute; left: 0; top: 38px; width: 592px; text-align: center;
    font-family: "Bebas Neue", system-ui, sans-serif; font-size: 52px; line-height: 1;
  }
  .front-title { left: 140px; top: 392px; width: 340px; }
  .front-title .title-line.first { font-size: 170px; }
  .front-title .title-small { font-size: 40px; margin: 4px 0; }
  .front-title .title-line.second { font-size: 146px; }
  .front-subtitle {
    position: absolute; left: 0; top: 756px; width: 592px; text-align: center;
    font-family: "Jost", system-ui, sans-serif; font-size: 16px; line-height: 22px;
    text-transform: uppercase;
  }
</style>
</head>
<body>
<main class="cover-wrap">

  <section class="back-cover">
    <div class="back-copy">
      <span class="logo-space"></span>
      <p>Lorem ipsum dolor sit amet, consectetur adipisicing elit, sed do eiusmod tempor incididunt ut labore et dolore magna aliqua. Ut enim ad minim veniam, quis nostrud exercitation ullamco laboris nisi ut aliquip ex ea commodo consequat. Duis aute irure dolor in reprehenderit in voluptate velit esse cillum dolore eu fugiat nulla pariatur. Excepteur sint occaecat cupidatat non proident, sunt in culpa qui officia deserunt mollit anim id est laborum. Sed ut perspiciatis unde omnis iste natus error sit voluptatem accusantium doloremque laudantium, totam rem aperiam, eaque ipsa quae ab illo inventore veritatis et quasi architecto beatae vitae dicta sunt explicabo. Nemo enim ipsam voluptatem quia voluptas sit aspernatur aut odit aut fugit, sed quia consequuntur magni dolores eos qui ratione voluptatem sequi nesciunt. Neque porro quisquam est, qui dolorem ipsum quia dolor sit amet, consectetur, adipisci velit, sed quia non numquam eius modi tempora incidunt ut labore et dolore magnam aliquam quaerat voluptatem.</p>
      <p>Lorem ipsum dolor sit amet, consectetur adipisicing elit, sed do eiusmod tempor incididunt ut labore et dolore magna aliqua. Ut enim ad minim veniam, quis nostrud exercitation ullamco laboris nisi ut aliquip ex ea commodo consequat. Duis aute irure dolor in reprehenderit in voluptate velit esse cillum dolore eu fugiat nulla pariatur. Excepteur sint occaecat cupidatat non proident, sunt in culpa qui officia deserunt mollit anim id est laborum. Sed ut perspiciatis unde omnis iste natus error sit voluptatem accusantium doloremque laudantium, totam rem aperiam, eaque ipsa quae ab illo inventore veritatis et quasi architecto beatae vitae dicta sunt explicabo. Nemo enim ipsam voluptatem quia voluptas sit aspernatur aut odit aut fugit, sed quia consequuntur magni dolores eos qui ratione voluptatem sequi nesciunt. Neque porro quisquam est, qui dolorem ipsum quia dolor sit amet, consectetur, adipisci velit, sed quia non numquam eius modi tempora inci-</p>
    </div>
    <h2 class="title-lockup back-title">
      <span class="title-line first">Chase</span>
      <span class="title-small">the</span>
      <span class="title-line second">Summit</span>
    </h2>
  </section>

  <section class="spine">
    <div class="spine-title">CHASE THE <span class="accent">SUMMIT</span></div>
    <div class="spine-author">AUTHOR’S NAME</div>
  </section>

  <section class="front-cover">
    <svg class="hero-photo" viewBox="0 0 569 470" role="img" aria-label="Photo of a businessman in a suit pulling open his shirt to reveal a blue hero costume, red cape flowing, above a hazy city skyline">
      <defs>
        <linearGradient id="sky" x1="0" y1="0" x2="1" y2="0.3">
          <stop offset="0" stop-color="var(--sky-amber)"/>
          <stop offset="0.45" stop-color="var(--sky-violet)"/>
          <stop offset="0.75" stop-color="var(--suit-navy)"/>
          <stop offset="1" stop-color="var(--cape-red)"/>
        </linearGradient>
        <radialGradient id="chest" cx="0.58" cy="0.42" r="0.22">
          <stop offset="0" stop-color="var(--chest-blue)" stop-opacity="0.8"/>
          <stop offset="1" stop-color="var(--chest-blue)" stop-opacity="0"/>
        </radialGradient>
        <linearGradient id="fade" x1="0" y1="0" x2="0" y2="1">
          <stop offset="0.6" stop-color="#000" stop-opacity="0"/>
          <stop offset="1" stop-color="#000" stop-opacity="1"/>
        </linearGradient>
      </defs>
      <rect width="569" height="470" fill="url(#sky)"/>
      <rect width="569" height="470" fill="url(#chest)"/>
      <rect width="569" height="470" fill="url(#fade)"/>
    </svg>

    <p class="front-author">AUTHOR’S NAME</p>

    <h1 class="title-lockup front-title">
      <span class="title-line first">Chase</span>
      <span class="title-small">the</span>
      <span class="title-line second">Summit</span>
    </h1>

    <p class="front-subtitle">How to accelerate your growth through<br>reaching out, getting a response from, and leaving<br>an impression on the people you admire most</p>
  </section>

</main>
</body>
</html>
```